PowerPoint Design Project for IT Consumerization presentation

I will be giving a presenatation using PP slides. The topic will the Brightfield is having. I will provide the content for the slides and there will be about 20 slides. I would like for the slides to be professional designed.

It Professional

```html
<!DOCTYPE html>
<html lang="en">
<head>
<meta charset="utf-8">
<title>Brightfield – slide set</title>
<link rel="stylesheet" href="https://fonts.googleapis.com/css2?family=Open+Sans:wght@400;600;700;800&family=Alfa+Slab+One&display=swap">
<style>
  :root {
    --backdrop: #c98b52;
    --slide-light: #ffffff;
    --slide-mid: #f3f3f3;
    --slide-edge: #d6d6d6;
    --ink: #3a3a3a;
    --ink-soft: #6a6a6a;
    --ink-faint: #8a8a8a;
    --bar: #58585a;
    --block: #000000;
    --table-head: #3d3d3f;
    --table-line: #dcdcdc;
    --node: #444446;
    --node-top: #6d6d70;
    --photo-a: #dfe7f0;
    --photo-b: #9fb4cc;
    --photo-c: #3c4f6a;
  }
  * { box-sizing: border-box; margin: 0; padding: 0; }
  html, body { width: 1200px; height: 689px; overflow: hidden; }
  body {
    position: relative;
    background: var(--backdrop);
    font-family: "Open Sans", Arial, sans-serif;
    color: var(--ink);
  }

  .slide {
    position: absolute;
    width: 254px;
    height: 192px;
    background: linear-gradient(90deg, var(--slide-light) 0%, var(--slide-mid) 55%, var(--slide-edge) 100%);
    box-shadow: 0 1px 3px rgba(0,0,0,.25);
    overflow: hidden;
  }
  .slide--title   { left: 371px; top: 19px; }
  .slide--intro   { left: 643px; top: 19px; }
  .slide--overview{ left: 37px;  top: 249px; }
  .slide--detail  { left: 336px; top: 249px; }
  .slide--table   { left: 621px; top: 249px; }
  .slide--diagram { left: 909px; top: 249px; }
  .slide--section { left: 37px;  top: 469px; }
  .slide--list    { left: 336px; top: 469px; }
  .slide--columns { left: 621px; top: 469px; }
  .slide--closing { left: 909px; top: 469px; }

  .footer-block { position: absolute; left: 0; bottom: 0; width: 24px; height: 12px; background: var(--block); }
  .footer-bar {
    position: absolute; left: 28px; right: 0; bottom: 0; height: 12px;
    background: var(--bar); color: #fff;
    font-size: 7px; font-weight: 700; letter-spacing: .5px;
    text-align: center; line-height: 12px;
  }

  .slide-heading {
    position: absolute; left: 22px; top: 15px;
    font-size: 10.5px; font-weight: 700; color: var(--ink); letter-spacing: .1px;
  }
  .brand {
    position: absolute; right: 20px; top: 13px;
    font-size: 11px; font-weight: 800; color: var(--ink); line-height: 1;
  }
  .brand-large {
    position: absolute; left: 0; right: 0; text-align: center;
    font-size: 27px; font-weight: 800; color: var(--ink); line-height: 1; letter-spacing: .3px;
  }

  .body-copy { position: absolute; font-size: 4.8px; line-height: 6.8px; color: var(--ink-soft); }

  .photo {
    position: absolute;
    background: linear-gradient(135deg, var(--photo-a) 0%, var(--photo-b) 55%, var(--photo-c) 100%);
    border: 1px solid #555;
  }

  .bullets { position: absolute; list-style: none; font-size: 5.6px; font-weight: 600; color: var(--ink); }
  .bullets li { position: relative; padding-left: 10px; }
  .bullets li::before {
    content: ""; position: absolute; left: 0; top: 50%;
    width: 5px; height: 5px; margin-top: -2.5px; border-radius: 50%; background: var(--ink);
  }

  .slide--title .brand-large { top: 50px; }
  .presentation-title { position: absolute; top: 99px; left: 0; right: 0; text-align: center; font-size: 13px; font-weight: 700; }
  .presentation-desc { position: absolute; top: 117px; left: 0; right: 0; text-align: center; font-size: 8px; }

  .slide--intro .body-copy { left: 24px; top: 42px; width: 210px; }
  .slide--intro .bullets { left: 24px; top: 101px; }
  .slide--intro .bullets li { line-height: 11.2px; }
  .slide--intro .photo { left: 134px; top: 100px; width: 98px; height: 66px; }

  .slide--overview .body-copy { left: 16px; top: 35px; width: 210px; }
  .slide--overview .photo { left: 64px; top: 83px; width: 124px; height: 83px; }

  .slide--detail .photo { left: 158px; top: 39px; width: 85px; height: 66px; }
  .slide--detail .copy-side { left: 19px; top: 37px; width: 134px; }
  .slide--detail .copy-full { left: 19px; top: 110px; width: 224px; }

  .data-table { position: absolute; left: 22px; top: 31px; width: 206px; border-collapse: collapse; }
  .data-table th {
    background: var(--table-head); color: #fff; font-size: 8.5px; font-weight: 700;
    height: 20px; text-align: center;
  }
  .data-table td {
    font-size: 4.8px; color: var(--ink-faint); height: 14.3px; padding-left: 10px;
    border-bottom: 1px solid var(--table-line); border-right: 1px solid var(--table-line); background: rgba(255,255,255,.6);
  }
  .data-table td:last-child { border-right: none; }

  .diagram { position: absolute; left: 0; top: 0; }

  .slide--section .brand-large { top: 30px; }
  .part-label { position: absolute; top: 80px; left: 0; right: 0; text-align: center; font-size: 15px; font-weight: 700; }
  .slide--section .body-copy { left: 24px; top: 102px; width: 206px; text-align: center; }

  .slide--list .bullets { left: 24px; top: 34px; }
  .slide--list .bullets li { line-height: 11.4px; }

  .column-block { position: absolute; width: 98px; font-size: 4.8px; line-height: 6px; color: var(--ink-soft); }
  .column-block h3 { font-size: 4.8px; font-weight: 700; color: var(--ink); line-height: 6px; }

  .slide--closing .brand-large { top: 46px; }
  .thanks { position: absolute; top: 100px; left: 0; right: 0; text-align: center; font-family: "Alfa Slab One", Georgia, serif; font-size: 16px; color: #2a2a2a; }
  .thanks-sub { position: absolute; top: 123px; left: 0; right: 0; text-align: center; font-size: 9.5px; font-weight: 700; color: #111; }
</style>
</head>
<body>

<section class="slide slide--title">
  <div class="brand-large">Brightfield</div>
  <h1 class="presentation-title">TITLE OF PRESENTATION</h1>
  <p class="presentation-desc">Description</p>
  <div class="footer-block"></div><div class="footer-bar">www.consumerdeck.com</div>
</section>

<section class="slide slide--intro">
  <h2 class="slide-heading">LOREM IPSUM&nbsp; LOREM</h2>
  <div class="brand">Brightfield</div>
  <p class="body-copy">Lorem ipsum dolor sit amet, consectetuer adipiscing elit, sed diam nonummy nibh euismod tincidunt ut laoreet dolore magna aliquam erat volutpat. Ut wisi enim ad minim veniam, quis nostrud exerci tation ullamcorper suscipit lobortis nisl ut aliquip ex ea commodo consequat. Duis autem vel eum iriure dolor in hendrerit in vulputate velit esse molestie consequat, vel illum dolore eu feugiat nulla facilisis.</p>
  <ul class="bullets">
    <li>Lorem ipsum&nbsp; Lorem ipsum</li>
    <li>Lorem ipsum Lorem Lorem</li>
    <li>Lorem ipsum Lorem ipsum</li>
    <li>Lorem ipsum orem Lorem ipsum</li>
    <li>Lorem ipsum Lorem</li>
  </ul>
  <div class="photo" role="img" aria-label="Photo of a wall of connected screens and devices"></div>
  <div class="footer-block"></div><div class="footer-bar">www.consumerdeck.com</div>
</section>

<section class="slide slide--overview">
  <h2 class="slide-heading">LOREM IPSUM&nbsp; LOREM</h2>
  <div class="brand">Brightfield</div>
  <p class="body-copy">Lorem ipsum dolor sit amet, consectetuer adipiscing elit, sed diam nonummy nibh euismod tincidunt ut laoreet dolore magna aliquam erat volutpat. Ut wisi enim ad minim veniam, quis nostrud exerci tation ullamcorper suscipit lobortis nisl ut aliquip ex ea commodo consequat.</p>
  <div class="photo" role="img" aria-label="Photo of a bright server room with blue cabling"></div>
  <div class="footer-block"></div><div class="footer-bar">www.consumerdeck.com</div>
</section>

<section class="slide slide--detail">
  <h2 class="slide-heading">LOREM IPSUM</h2>
  <div class="brand">Brightfield</div>
  <p class="body-copy copy-side">Lorem ipsum dolor sit amet, consectetuer adipiscing elit, sed diam nonummy nibh euismod tincidunt ut laoreet dolore magna aliquam erat volutpat. Ut wisi enim ad minim veniam, quis nostrud exerci tation ullamcorper suscipit lobortis nisl ut aliquip ex ea commodo consequat. Duis autem vel eum iriure dolor in hendrerit in vulputate velit esse molestie consequat, vel illum dolore eu feugiat nulla facilisis.</p>
  <p class="body-copy copy-full">Lorem ipsum dolor sit amet, consectetuer adipiscing elit, sed diam nonummy nibh euismod tincidunt ut laoreet dolore magna aliquam erat volutpat. Ut wisi enim ad minim veniam, quis nostrud exerci tation ullamcorper suscipit lobortis nisl ut aliquip ex ea commodo consequat.</p>
  <div class="photo" role="img" aria-label="Photo of network cables plugged into a patch panel"></div>
  <div class="footer-block"></div><div class="footer-bar">www.consumerdeck.com</div>
</section>

<section class="slide slide--table">
  <h2 class="slide-heading">LOREM IPSUM</h2>
  <div class="brand">Brightfield</div>
  <table class="data-table">
    <thead><tr><th colspan="4">Lorem ipsum&nbsp; Lorem ipsum&nbsp; Lorem ipsum</th></tr></thead>
    <tbody>
      <tr><td>Lorem ipsum</td><td>Lorem ipsum</td><td>Lorem ipsum</td><td>Lorem ipsum</td></tr>
      <tr><td>Lorem ipsum</td><td>Lorem ipsum</td><td>Lorem ipsum</td><td>Lorem ipsum</td></tr>
      <tr><td>Lorem ipsum</td><td>Lorem ipsum</td><td>Lorem ipsum</td><td>Lorem ipsum</td></tr>
      <tr><td>Lorem ipsum</td><td>Lorem ipsum</td><td>Lorem ipsum</td><td>Lorem ipsum</td></tr>
      <tr><td>Lorem ipsum</td><td>Lorem ipsum</td><td>Lorem ipsum</td><td>Lorem ipsum</td></tr>
      <tr><td>Lorem ipsum</td><td>Lorem ipsum</td><td>Lorem ipsum</td><td>Lorem ipsum</td></tr>
      <tr><td>Lorem ipsum</td><td>Lorem ipsum</td><td>Lorem ipsum</td><td>Lorem ipsum</td></tr>
    </tbody>
  </table>
  <div class="footer-block"></div><div class="footer-bar">www.consumerdeck.com</div>
</section>

<section class="slide slide--diagram">
  <h2 class="slide-heading">LOREM IPSUM</h2>
  <div class="brand">Brightfield</div>
  <svg class="diagram" width="254" height="192" viewBox="0 0 254 192" font-family="Open Sans, Arial, sans-serif" font-weight="700">
    <defs>
      <g id="drum">
        <rect x="0" y="3" width="32" height="22" fill="var(--node)"/>
        <ellipse cx="16" cy="25" rx="16" ry="3" fill="var(--node)"/>
        <ellipse cx="16" cy="3" rx="16" ry="3" fill="var(--node-top)"/>
      </g>
    </defs>
    <g stroke="#9a9a9a" stroke-width=".6" fill="none">
      <path d="M28 50 V114 M28 80 H37 M28 114 H37"/>
      <path d="M78 50 V146 M78 80 H87 M78 114 H87 M78 146 H87"/>
      <path d="M129 50 V146 M129 80 H138 M129 114 H138 M129 146 H138"/>
      <path d="M178 50 V146 M178 80 H187 M178 114 H187 M178 146 H187"/>
      <path d="M73 50 H78 M124 50 H129 M173 50 H178"/>
    </g>
    <g fill="var(--node)">
      <rect x="32" y="42" width="41" height="16" rx="2"/>
      <rect x="82" y="42" width="41" height="16" rx="2"/>
      <rect x="133" y="42" width="41" height="16" rx="2"/>
      <rect x="182" y="42" width="41" height="16" rx="2"/>
    </g>
    <g fill="#fff" font-size="4.8" text-anchor="middle">
      <text x="52.5" y="52">Lorem ipsum</text>
      <text x="102.5" y="52">Lorem ipsum</text>
      <text x="153.5" y="52">Lorem ipsum</text>
      <text x="202.5" y="52">Lorem ipsum</text>
    </g>
    <use href="#drum" x="37" y="66"/><use href="#drum" x="37" y="99"/>
    <use href="#drum" x="87" y="66"/><use href="#drum" x="87" y="99"/><use href="#drum" x="87" y="132"/>
    <use href="#drum" x="138" y="66"/><use href="#drum" x="138" y="99"/><use href="#drum" x="138" y="132"/>
    <use href="#drum" x="187" y="66"/><use href="#drum" x="187" y="99"/><use href="#drum" x="187" y="132"/>
    <g fill="#fff" font-size="4.8" text-anchor="middle">
      <text x="53" y="83">Lorem</text><text x="53" y="116">Lorem</text>
      <text x="103" y="83">Lorem</text><text x="103" y="116">Lorem</text><text x="103" y="149">Lorem</text>
      <text x="154" y="83">Lorem</text><text x="154" y="116">Lorem</text><text x="154" y="149">Lorem</text>
      <text x="203" y="83">Lorem</text><text x="203" y="116">Lorem</text><text x="203" y="149">Lorem</text>
    </g>
  </svg>
  <div class="footer-block"></div><div class="footer-bar">www.consumerdeck.com</div>
</section>

<section class="slide slide--section">
  <div class="brand-large">Brightfield</div>
  <h2 class="part-label">PART 3</h2>
  <p class="body-copy">Lorem ipsum dolor sit amet, consectetuer adipiscing elit, sed diam nonummy nibh euismod tincidunt ut laoreet dolore magna aliquam erat volutpat. Ut wisi enim ad minim veniam, quis nostrud exerci tation ullamcorper suscipit lobortis nisl ut aliquip ex ea commodo consequat. Duis autem vel eum iriure dolor in hendrerit in vulputate velit esse molestie consequat, vel illum dolore eu feugiat nulla facilisis.</p>
  <div class="footer-block"></div><div class="footer-bar">www.consumerdeck.com</div>
</section>

<section class="slide slide--list">
  <h2 class="slide-heading">LOREM IPSUM</h2>
  <div class="brand">Brightfield</div>
  <ul class="bullets">
    <li>Lorem ipsum Lorem Lorem ipsum Lorem</li>
    <li>Lorem ipsum Lorem Lorem</li>
    <li>Lorem ipsum Lorem Lorem ipsum&nbsp; Lorem&nbsp; Lorem ipsum</li>
    <li>Lorem ipsum orem Lorem ipsum&nbsp; Lo</li>
    <li>Lorem ipsum Lorem</li>
    <li>Lorem ipsum Lorem Lorem ipsum&nbsp; Lorem</li>
    <li>Lorem ipsum Lorem Lorem</li>
    <li>Lorem ipsum Lorem Lorem ipsum&nbsp; Lorem&nbsp; Lorem ipsum</li>
    <li>Lorem ipsum orem Lorem ipsum&nbsp; Lo</li>
    <li>Lorem ipsum Lorem</li>
  </ul>
  <div class="footer-block"></div><div class="footer-bar">www.consumerdeck.com</div>
</section>

<section class="slide slide--columns">
  <h2 class="slide-heading">LOREM IPSUM</h2>
  <div class="brand">Brightfield</div>
  <div class="column-block" style="left:20px;top:35px"><h3>Sub Title-1</h3>Lorem ipsum dolor sit amet, etuer. Lorem ipsum dolor sit amet, etuer. Lorem ipsum dolor sit amet.</div>
  <div class="column-block" style="left:20px;top:75px"><h3>Sub Title-2</h3>Lorem ipsum dolor sit amet, etuer. Lorem ipsum dolor sit amet, etuer. Lorem ipsum dolor sit amet.</div>
  <div class="column-block" style="left:20px;top:115px"><h3>Sub Title-3</h3>Lorem ipsum dolor sit amet, etuer. Lorem ipsum dolor sit amet, etuer. Lorem ipsum dolor sit amet.</div>
  <div class="column-block" style="left:134px;top:35px"><h3>Sub Title-1</h3>Lorem ipsum dolor sit amet, etuer. Lorem ipsum dolor sit amet, etuer. Lorem ipsum dolor sit amet.</div>
  <div class="column-block" style="left:134px;top:75px"><h3>Sub Title-2</h3>Lorem ipsum dolor sit amet, etuer. Lorem ipsum dolor sit amet, etuer. Lorem ipsum dolor sit amet.</div>
  <div class="column-block" style="left:134px;top:115px"><h3>Sub Title-3</h3>Lorem ipsum dolor sit amet, etuer. Lorem ipsum dolor sit amet, etuer. Lorem ipsum dolor sit amet.</div>
  <div class="footer-block"></div><div class="footer-bar">www.consumerdeck.com</div>
</section>

<section class="slide slide--closing">
  <div class="brand-large">Brightfield</div>
  <p class="thanks">Thank You!</p>
  <p class="thanks-sub">For your attention</p>
  <div class="footer-block"></div><div class="footer-bar">www.consumerdeck.com</div>
</section>

</body>
</html>
```